Business Cards

Business cards (double-sided) to be handed out to clients and potential clients, with contact details, logo .

Target Market(s)

Small to medium size businesses

Industry/Entity Type

Accountants

Contact Information for Business Card

Brightwater Ledger & Counsel Ltd

Colors

Designer to choose only greyscale colors for use in the design.

Requirements
Must have
• Name, Title, Address, Phone number, Email, Website
Nice to have
• Modern, clean lines, classy
Should not have
• Business cards to be double-sided. Form keeps reverting to single-sided.

```html
<!DOCTYPE html>
<html lang="en">
<head>
<meta charset="utf-8">
<title>Brightwater Ledger &amp; Counsel – Business Cards</title>
<link rel="stylesheet" href="https://fonts.googleapis.com/css2?family=Lato:wght@300;400;700&display=swap">
<style>
  :root {
    --backdrop: #c4c5c5;
    --card: #1c1d1f;
    --card-edge: #26282a;
    --rail: #2a2b2e;
    --ink: #f2f2f2;
    --ink-soft: #c9cacc;
    --icon: #bfc0c2;
  }
  * { box-sizing: border-box; margin: 0; padding: 0; }
  html, body { width: 1200px; height: 900px; overflow: hidden; }
  body {
    background: var(--backdrop);
    font-family: "Lato", sans-serif;
    color: var(--ink);
    display: flex;
    flex-direction: column;
    align-items: center;
    justify-content: center;
    gap: 56px;
  }
  .card {
    width: 630px;
    height: 360px;
    background: var(--card);
    border: 1px solid var(--card-edge);
    position: relative;
  }
  .brand {
    display: flex;
    align-items: center;
    gap: 14px;
  }
  .brand-mark {
    width: 14px;
    height: 14px;
    background: var(--ink);
    flex: none;
  }
  .brand-name {
    font-weight: 300;
    letter-spacing: 0.12em;
    text-transform: uppercase;
    color: var(--ink);
    line-height: 1.3;
  }
  .card-front { display: flex; align-items: center; justify-content: center; }
  .card-front .brand-name { font-size: 24px; max-width: 360px; }

  .card-back .brand { position: absolute; left: 48px; top: 50%; transform: translateY(-50%); }
  .card-back .brand-name { font-size: 17px; max-width: 210px; }

  .contact-rail {
    position: absolute;
    left: 318px;
    top: 70px;
    width: 46px;
    height: 220px;
    border-radius: 23px;
    background: var(--rail);
    display: flex;
    flex-direction: column;
    align-items: center;
    padding-top: 10px;
    gap: 0;
  }
  .rail-avatar {
    width: 34px; height: 34px; border-radius: 50%;
    background: #16171a;
    display: flex; align-items: center; justify-content: center;
    margin-bottom: 20px;
  }
  .rail-icon { width: 16px; height: 16px; margin-bottom: 20px; }
  .rail-icon svg, .rail-avatar svg { display: block; }

  .contact-details {
    position: absolute;
    left: 384px;
    top: 66px;
    font-size: 12.5px;
    color: var(--ink-soft);
  }
  .person-name { font-size: 20px; font-weight: 700; letter-spacing: 0.04em; color: var(--ink); text-transform: uppercase; }
  .person-title { font-size: 14px; color: var(--ink); margin-bottom: 18px; }
  .detail { line-height: 1.25; }
  .detail-address { margin-bottom: 14px; }
  .detail-line { height: 36px; display: flex; align-items: center; }
</style>
</head>
<body>
  <section class="card card-front" aria-label="Business card front">
    <div class="brand">
      <span class="brand-mark"></span>
      <span class="brand-name">Brightwater Ledger &amp; Counsel Ltd</span>
    </div>
  </section>

  <section class="card card-back" aria-label="Business card back">
    <div class="brand">
      <span class="brand-mark"></span>
      <span class="brand-name">Brightwater Ledger &amp; Counsel Ltd</span>
    </div>

    <div class="contact-rail">
      <div class="rail-avatar">
        <svg width="18" height="18" viewBox="0 0 18 18" fill="none" stroke="var(--icon)" stroke-width="1.3">
          <circle cx="9" cy="6" r="3.2"/>
          <path d="M2.5 16c0-3.6 2.9-5.6 6.5-5.6s6.5 2 6.5 5.6"/>
        </svg>
      </div>
      <div class="rail-icon">
        <svg width="16" height="16" viewBox="0 0 16 16" fill="none" stroke="var(--icon)" stroke-width="1.2">
          <path d="M8 15s5-5 5-8.5A5 5 0 0 0 3 6.5C3 10 8 15 8 15z"/>
          <circle cx="8" cy="6.5" r="1.8"/>
        </svg>
      </div>
      <div class="rail-icon">
        <svg width="16" height="16" viewBox="0 0 16 16" fill="none" stroke="var(--icon)" stroke-width="1.2">
          <path d="M4 1.5l2.2 3-1.4 1.6a8 8 0 0 0 5.1 5.1l1.6-1.4 3 2.2-1.3 2.2C8 14.5 1.5 8 1.8 2.8z"/>
        </svg>
      </div>
      <div class="rail-icon">
        <svg width="16" height="16" viewBox="0 0 16 16" fill="none" stroke="var(--icon)" stroke-width="1.2">
          <rect x="1.5" y="3.5" width="13" height="9"/>
          <path d="M1.5 3.5L8 9l6.5-5.5"/>
        </svg>
      </div>
      <div class="rail-icon">
        <svg width="16" height="16" viewBox="0 0 16 16" fill="none" stroke="var(--icon)" stroke-width="1.2">
          <circle cx="8" cy="8" r="6.5"/>
          <ellipse cx="8" cy="8" rx="2.8" ry="6.5"/>
          <path d="M1.5 8h13"/>
        </svg>
      </div>
    </div>

    <div class="contact-details">
      <p class="person-name">Maren Holt</p>
      <p class="person-title">CEO</p>
      <p class="detail detail-address">Level 3, 48 Harlow Lane,<br>Westbrook, NY 10482</p>
      <p class="detail detail-line">555 014 2287</p>
      <p class="detail detail-line">hello@brightwaterledger.com</p>
      <p class="detail detail-line">brightwaterledger.com</p>
    </div>
  </section>
</body>
</html>
```